LETTERHEAD & ENVELOPE: eye-catching stationary design for our custom office furniture business

Our company recently rebranded and we are in need of new stationary. Specifically, we need branded letterhead for standard paper size (8.5” x 11”), and matching envelopes, size: #9.

All designs should incorporate our brand colors, brand typeface, and logo. Please view attached brand guidelines document for brand colors, and brand description.

Letterhead: 8.5” x 11” Must include CoralvexKTN Logo, Dorrit Falke Certified Dealer Logo, mailing address, phone number, website, and email address.

Envelope: 9.5” x 4.125” Must include CoralvexKTN Logo, mailing address, and Dorrit Falke Certified Dealer Logo.

Attached files include:

```html
<!DOCTYPE html>
<html lang="en">
<head>
<meta charset="utf-8">
<title>CoralvexKTN Stationery</title>
<link href="https://fonts.googleapis.com/css2?family=Raleway:wght@400;500&family=Montserrat:wght@400;500&family=Arimo:wght@400&display=swap" rel="stylesheet">
<style>
  :root {
    --brand-green: #5e7d6e;
    --paper: #ffffff;
    --backdrop: #a7c4e1;
    --ink: #333333;
    --ink-soft: #8c8c8c;
    --ink-faint: #a5a5a5;
    --dealer-red: #e8401c;
    --rule: #555555;
  }
  * { margin: 0; padding: 0; box-sizing: border-box; }
  html, body { width: 1200px; height: 1200px; overflow: hidden; }
  body { background: var(--backdrop); position: relative; font-family: "Montserrat", sans-serif; color: var(--ink); }

  .sheet { position: absolute; background: var(--paper); overflow: hidden; }
  .wave { position: absolute; left: 0; top: 0; width: 100%; display: block; }

  .brand { position: absolute; display: flex; align-items: center; }
  .brand-dot { border-radius: 50%; background: var(--brand-green); flex: none; }
  .brand-name { font-family: "Raleway", sans-serif; font-weight: 400; color: var(--brand-green); letter-spacing: 0.2px; }

  /* Letterhead */
  .letterhead { left: 49px; top: 250px; width: 483px; height: 682px; }
  .letterhead .wave { height: 44px; }
  .letterhead .brand { left: 48px; top: 30px; gap: 10px; }
  .letterhead .brand-dot { width: 29px; height: 29px; }
  .letterhead .brand-name { font-size: 24px; }

  .recipient { position: absolute; left: 50px; top: 152px; }
  .recipient-label { font-size: 8.5px; letter-spacing: 1.5px; }
  .recipient-name { font-size: 7.5px; font-weight: 500; margin-top: 5px; }
  .recipient-lines { font-size: 6px; color: var(--ink-faint); line-height: 10.5px; margin-top: 2px; }
  .letter-date { position: absolute; right: 49px; top: 153px; font-size: 6.2px; color: var(--ink-soft); }

  .letter-body { position: absolute; left: 50px; top: 244px; width: 385px; font-size: 6.2px; line-height: 8.4px; color: var(--ink-faint); text-align: justify; }
  .letter-body p { margin-bottom: 8.6px; }

  .signature { position: absolute; left: 49px; top: 478px; width: 86px; height: 20px; background: #ececec; border-radius: 2px; }
  .signer { position: absolute; left: 48px; top: 508px; }
  .signer-name { font-size: 7.5px; letter-spacing: 0.4px; }
  .signer-role { font-size: 5.5px; color: var(--ink-faint); margin-top: 2px; }

  .letter-footer { position: absolute; left: 48px; top: 626px; width: 388px; height: 32px; font-family: "Arimo", sans-serif; font-size: 7.6px; color: #444; }
  .contact-list { position: absolute; left: 0; top: 0; line-height: 9.8px; }
  .contact-list li { list-style: none; display: flex; align-items: center; gap: 4px; }
  .contact-list svg { width: 6px; height: 6px; fill: var(--brand-green); }
  .footer-rule { position: absolute; top: 0; width: 1px; height: 31px; background: var(--rule); }
  .footer-rule.first { left: 157px; }
  .footer-rule.second { left: 277px; }
  .footer-address { position: absolute; left: 181px; top: 0; line-height: 9.8px; }
  .dealer { position: absolute; right: 0; top: 9px; display: flex; align-items: center; gap: 6px; }
  .dealer-dot { width: 16px; height: 16px; border-radius: 50%; background: var(--dealer-red); }
  .dealer-name { font-family: "Arimo", sans-serif; font-size: 8.4px; color: var(--dealer-red); }

  /* Envelope front */
  .envelope-front { left: 572px; top: 298px; width: 576px; height: 251px; }
  .envelope-front .wave { height: 52px; }
  .envelope-front .brand { left: 21px; top: 40px; gap: 10px; }
  .envelope-front .brand-dot { width: 28px; height: 28px; }
  .envelope-front .brand-name { font-size: 23px; }
  .return-address { position: absolute; left: 21px; top: 75px; font-family: "Arimo", sans-serif; font-size: 8.2px; line-height: 10px; color: #555; }

  /* Envelope back */
  .envelope-back { left: 572px; top: 631px; width: 578px; height: 251px; }
  .envelope-back .flap { position: absolute; left: 0; top: 0; width: 100%; height: 75px; }
  .envelope-back .flap-dot { position: absolute; left: 267px; top: 13px; width: 44px; height: 44px; border-radius: 50%; background: var(--brand-green); }
</style>
</head>
<body>

  <section class="sheet letterhead" aria-label="Letterhead">
    <svg class="wave" viewBox="0 0 604 55" preserveAspectRatio="none" aria-hidden="true">
      <path d="M0 0 H604 V52 C540 50 470 44 400 33 C300 17 190 10 0 40 Z" fill="var(--brand-green)"/>
      <path d="M0 31 C70 18 150 12 205 13" stroke="#fff" stroke-width="3" fill="none"/>
      <path d="M395 36 C470 46 540 48 604 40" stroke="#fff" stroke-width="3" fill="none"/>
    </svg>

    <div class="brand">
      <span class="brand-dot"></span>
      <span class="brand-name">CoralvexKTN</span>
    </div>

    <div class="recipient">
      <div class="recipient-label">TO</div>
      <div class="recipient-name">Ellis Varnholt</div>
      <div class="recipient-lines">
        Human Resources<br>
        Brightfold Inc.<br>
        2207-B Ostrander, Wellmere<br>
        K41 USA
      </div>
    </div>
    <div class="letter-date">Friday, 01/01/2018</div>

    <div class="letter-body">
      <p>Lorem ipsum dolor sit amet, consectetuer adipiscing elit, sed diam nonummy nibh euismod tincidunt ut laoreet dolore magna aliquam erat volutpat. Ut wisi enim ad minim veniam, quis nostrud exerci tation ullamcorper suscipit lobortis nisl ut aliquip ex ea commodo consequat. Duis autem vel eum iriure dolor in hendrerit in vulputate velit esse molestie consequat, vel illum dolore eu feugiat nulla facilisis at vero eros et accumsan et iusto odio dignissim qui blandit praesent luptatum zzril delenit augue duis dolore te feugait nulla facilisi.</p>
      <p>Nam liber tempor cum soluta nobis eleifend option congue nihil imperdiet doming id quod mazim placerat facer possim assum. Typi non habent claritatem insitam.</p>
      <p>Est usus legentis in iis qui facit eorum claritatem.</p>
      <p>Investigationes demonstraverunt lectores legere me lius quod ii legunt saepius. Claritas est etiam processus dynamicus, qui sequitur mutationem consuetudium lectorum. Mirum est notare quam littera gothica, quam nunc putamus parum claram, anteposuerit litterarum formas humanitatis per seacula quarta decima et quinta decima. Eodem modo typi, qui nunc nobis videntur parum clari, fiant sollemnes in futurum.</p>
      <p>consectetuer adipiscing elit, sed diam nonummy nibh euismod tincidunt ut laoreet dolore magna aliquam erat volutpat. Ut wisi enim ad minim veniam, quis nostrud exerci tation ullamcorper suscipit lobortis nisl ut aliquip ex ea commodo consequat. Duis autem vel eum iriure dolor in hendrerit in vulputate velit esse molestie consequat, vel illum dolore eu feugiat nulla facilisis at vero eros et accumsan et iusto odio dignissim qui blandit praesent luptatum zzril delenit augue duis dolore te feugait nulla facilisi.</p>
      <p>Nam liber tempor cum soluta nobis eleifend option congue nihil imperdiet .</p>
    </div>

    <div class="signature" role="img" aria-label="Handwritten signature of Adrian Moller"></div>
    <div class="signer">
      <div class="signer-name">Adrian Moller</div>
      <div class="signer-role">Managing Director</div>
    </div>

    <footer class="letter-footer">
      <ul class="contact-list">
        <li><svg viewBox="0 0 10 10"><path d="M2 0 L4 2.5 L3 3.8 C3.8 5.5 4.8 6.4 6.2 7 L7.5 6 L10 8 L8.5 10 C4 9.5 0.5 6 0 1.5 Z"/></svg>555.014.2873</li>
        <li><svg viewBox="0 0 10 10"><path d="M0 2 H10 V8 H0 Z M0.8 2.6 L5 5.6 L9.2 2.6" stroke="#fff" stroke-width="0.8"/></svg>hello@coralvexktn.com</li>
        <li><svg viewBox="0 0 10 10"><circle cx="5" cy="5" r="5"/><path d="M0 5 H10 M5 0 C2 3 2 7 5 10 M5 0 C8 3 8 7 5 10" stroke="#fff" stroke-width="0.7" fill="none"/></svg>www.coralvexktn.com</li>
      </ul>
      <span class="footer-rule first"></span>
      <address class="footer-address" style="font-style:normal">410 NW Larkspur<br>Suite 120<br>Halden, OR 97000</address>
      <span class="footer-rule second"></span>
      <div class="dealer">
        <span class="dealer-dot"></span>
        <span class="dealer-name">Dorrit Falke Certified Dealer</span>
      </div>
    </footer>
  </section>

  <section class="sheet envelope-front" aria-label="Envelope front">
    <svg class="wave" viewBox="0 0 720 65" preserveAspectRatio="none" aria-hidden="true">
      <path d="M0 0 H720 V63 C640 60 560 52 470 40 C350 20 220 12 0 45 Z" fill="var(--brand-green)"/>
      <path d="M0 35 C80 22 170 16 240 17" stroke="#fff" stroke-width="3.5" fill="none"/>
      <path d="M470 44 C560 56 650 59 720 50" stroke="#fff" stroke-width="3.5" fill="none"/>
    </svg>
    <div class="brand">
      <span class="brand-dot"></span>
      <span class="brand-name">CoralvexKTN</span>
    </div>
    <address class="return-address" style="font-style:normal">410 NW Larkspur, Suite 120<br>Halden, OR 97000</address>
  </section>

  <section class="sheet envelope-back" aria-label="Envelope back">
    <svg class="flap" viewBox="0 0 578 75" preserveAspectRatio="none" aria-hidden="true">
      <path d="M12 0 L26 54 C29 64 36 70 48 70 H530 C542 70 550 64 553 54 L567 0" stroke="#d2d2d2" stroke-width="1.5" fill="#fff"/>
    </svg>
    <span class="flap-dot"></span>
  </section>

</body>
</html>
```